Alternative Therapy Service Needs Compelling Brochure Design

Beyond the Meadow, LLC is looking for a brochure design that will capture the attention of others looking for support both mentally and physically. Colors that are soothing, convey support, growth, and strength are key!
The colors in my logo are great and a play or combo of any of those would be great....I am hoping the brochure can feel like an oasis from one's everyday life....I also love the tree concept of my logo as trees convey the growth and support that Beyond the Meadow offers...I am excited to see what you can create!

Hello All Designers! I am looking for a design on the outside and inside of the brochure...tri-fold or bi-fold brochures work! Please do not be concerned with adding text from my website into it as I am adding new services and will be updating the website ASAP I would like the brochure to be editable and easy to add and delete from as I change my business and add new elements and people to my staff... Thanks for all your contribution to my brochure project!

Reason: There are many designers who were invited later in the process and I would like to give them more time to design!

Industry/Entity Type

It Service

```html
<!DOCTYPE html>
<html lang="en">
<head>
<meta charset="utf-8">
<title>Beyond the Meadow — Brochure Inside Spread</title>
<link href="https://fonts.googleapis.com/css2?family=Arimo:wght@400;700&display=swap" rel="stylesheet">
<style>
  :root {
    --blue: #1c6cbd;
    --blue-deep: #1565b4;
    --green: #7dbb36;
    --green-dark: #5aa52e;
    --lime: #c9d92a;
    --yellow: #e6e51f;
    --text: #333333;
    --ink: #111111;
    --paper: #ffffff;
    --meadow-light: #e9dcb6;
    --meadow-mid: #c7b27c;
    --meadow-sky: #f4ecd2;
  }
  * { margin: 0; padding: 0; box-sizing: border-box; }
  html, body { width: 1200px; height: 928px; overflow: hidden; background: var(--paper); }
  .spread {
    position: relative; width: 1200px; height: 928px; overflow: hidden;
    background: var(--paper); font-family: "Arimo", Arial, sans-serif; color: var(--text);
  }
  .backdrop { position: absolute; inset: 0; }
  .column { position: absolute; }
  .col-left { left: 48px; width: 356px; }
  .col-mid { left: 428px; width: 344px; }
  .col-right { left: 816px; width: 346px; }
  .row-top { top: 52px; }
  .row-main { top: 232px; }
  .section-title {
    font-weight: 700; font-size: 21px; letter-spacing: 0.2px;
    text-align: center; margin-bottom: 10px; color: var(--blue);
  }
  .section-title.is-green { color: var(--green); }
  .body-copy { font-size: 11.2px; line-height: 16px; margin-bottom: 16px; }
  .body-copy.is-centered { text-align: center; }
  .body-copy.narrow-1 { padding-left: 60px; }
  .body-copy.stub { width: 80px; }
  .brand {
    position: absolute; left: 40px; top: 668px;
    display: flex; align-items: center; gap: 8px;
    font-size: 17px; font-weight: 700; color: var(--paper);
  }
  .brand-dot { width: 16px; height: 16px; border-radius: 50%; background: var(--yellow); }
  .closing { position: absolute; left: 52px; top: 766px; width: 510px; color: var(--ink); }
  .closing .section-title { color: var(--ink); text-align: left; font-size: 22px; margin-bottom: 8px; }
  .closing .body-copy { color: var(--ink); font-size: 11.2px; line-height: 15.5px; }
</style>
</head>
<body>
<main class="spread">
  <svg class="backdrop" width="1200" height="928" viewBox="0 0 1200 928" aria-hidden="true">
    <defs>
      <linearGradient id="meadowGreen" x1="0" y1="0" x2="1" y2="0">
        <stop offset="0" stop-color="var(--green-dark)"/>
        <stop offset="0.55" stop-color="var(--green)"/>
        <stop offset="1" stop-color="var(--yellow)"/>
      </linearGradient>
      <linearGradient id="swoosh" x1="0" y1="1" x2="1" y2="0">
        <stop offset="0" stop-color="var(--blue-deep)"/>
        <stop offset="1" stop-color="#2b86d1"/>
      </linearGradient>
      <linearGradient id="photoTone" x1="0" y1="0" x2="0" y2="1">
        <stop offset="0" stop-color="var(--meadow-sky)"/>
        <stop offset="0.5" stop-color="var(--meadow-light)"/>
        <stop offset="1" stop-color="var(--meadow-mid)"/>
      </linearGradient>
    </defs>
    <path class="green-wave" fill="url(#meadowGreen)"
      d="M0,612 C160,630 330,700 520,692 C720,684 880,580 1200,552 L1200,928 L0,928 Z"/>
    <path class="lime-band" fill="var(--lime)"
      d="M480,928 C560,790 700,650 900,590 C1020,556 1130,550 1200,556 L1200,574 C1120,566 1010,574 905,606 C720,664 590,800 520,928 Z"/>
    <path class="blue-swoosh" fill="url(#swoosh)"
      d="M520,928 C590,800 720,664 905,606 C1010,574 1120,566 1200,574 L1200,600 C1110,590 1000,600 900,634 C760,684 660,800 600,928 Z"/>
  </svg>

  <svg style="position:absolute;left:0;top:0" width="1200" height="928" viewBox="0 0 1200 928"
       role="img" aria-label="Photograph of a smiling woman with arms open in a sunlit meadow">
    <path fill="url(#photoTone)"
      d="M600,928 C660,800 760,684 900,634 C1000,600 1110,590 1200,600 L1200,928 Z"/>
  </svg>

  <section class="column col-left row-top">
    <h2 class="section-title">LOREM IMPOSUM</h2>
    <p class="body-copy">Lorem ipsum dolor sit amet, consectetur adipisicing elit, sed do eiusmod tempor incididunt ut labore et dolore magna aliqua. Ut enim ad minim veniam, quis nostrud exercitation ullamco laboris nisi ut aliquip ex ea commodo consequat. Duis aute irure dolor in reprehenderit in voluptate velit esse cillum dolore eu fugiat nulla pariatur. Excepteur sint occaecat cupidatat non proident, sunt in culpa qui officia deserunt mollit anim id est laborum.</p>
  </section>
  <section class="column col-mid row-top">
    <h2 class="section-title is-green">LOREM IMPOSUM</h2>
    <p class="body-copy">Lorem ipsum dolor sit amet, consectetur adipisicing elit, sed do eiusmod tempor incididunt ut labore et dolore magna aliqua. Ut enim ad minim veniam, quis nostrud exercitation ullamco laboris nisi ut aliquip ex ea commodo consequat. Duis aute irure dolor in reprehenderit in voluptate velit esse cillum dolore eu fugiat nulla pariatur. Excepteur sint occaecat cupidatat non proident, sunt in culpa qui officia deserunt mollit anim id est laborum.</p>
  </section>
  <section class="column col-right row-top">
    <h2 class="section-title">LOREM IMPOSUM</h2>
    <p class="body-copy">Lorem ipsum dolor sit amet, consectetur adipisicing elit, sed do eiusmod tempor incididunt ut labore et dolore magna aliqua. Ut enim ad minim veniam, quis nostrud exercitation ullamco laboris nisi ut aliquip ex ea commodo consequat. Duis aute irure dolor in reprehenderit in voluptate velit esse cillum dolore eu fugiat nulla pariatur. Excepteur sint occaecat cupidatat non proident, sunt in culpa qui officia deserunt mollit anim id est laborum.</p>
  </section>

  <section class="column col-left row-main">
    <h2 class="section-title">LOREM IMPOSUM</h2>
    <p class="body-copy">Lorem ipsum dolor sit amet, consectetur adipisicing elit, sed do eiusmod tempor incididunt ut labore et dolore magna aliqua. Ut enim ad minim veniam, quis nostrud exercitation ullamco laboris nisi ut aliquip ex ea commodo consequat. Duis aute irure dolor in reprehenderit in voluptate velit esse cillum dolore eu fugiat nulla pariatur. Excepteur sint occaecat cupidatat non proident, sunt in culpa qui officia deserunt mollit anim id est laborum.</p>
    <p class="body-copy">Lorem ipsum dolor sit amet, consectetur adipisicing elit, sed do eiusmod tempor incididunt ut labore et dolore magna aliqua. Ut enim ad minim veniam, quis nostrud exercitation ullamco laboris nisi ut aliquip ex ea commodo consequat. Duis aute irure dolor in reprehenderit in voluptate velit esse cillum dolore eu fugiat nulla pariatur. Excepteur sint occaecat cupidatat non proident, sunt in culpa qui officia deserunt mollit anim id est laborum.</p>
    <p class="body-copy narrow-1">Lorem ipsum dolor sit amet, consectetur adipisicing elit, sed do eiusmod tempor incididunt ut labore et dolore magna aliqua. Ut enim ad minim veniam, quis nostrud exercitation ullamco laboris nisi ut aliquip ex ea commodo consequat. Duis aute irure dolor in reprehenderit in voluptate velit esse cillum dolore eu fugiat nulla pariatur.</p>
  </section>
  <section class="column col-mid row-main">
    <h2 class="section-title is-green">LOREM IMPOSUM</h2>
    <p class="body-copy">Lorem ipsum dolor sit amet, consectetur adipisicing elit, sed do eiusmod tempor incididunt ut labore et dolore magna aliqua. Ut enim ad minim veniam, quis nostrud exercitation ullamco laboris nisi ut aliquip ex ea commodo consequat. Duis aute irure dolor in reprehenderit in voluptate velit esse cillum dolore eu fugiat nulla pariatur. Excepteur sint occaecat cupidatat non proident, sunt in culpa qui officia deserunt mollit anim id est laborum.</p>
    <p class="body-copy">Lorem ipsum dolor sit amet, consectetur adipisicing elit, sed do eiusmod tempor incididunt ut labore et dolore magna aliqua. Ut enim ad minim veniam, quis nostrud exercitation ullamco laboris nisi ut aliquip ex ea commodo consequat. Duis aute irure dolor in reprehenderit in voluptate velit esse cillum dolore eu fugiat nulla pariatur. Excepteur sint occaecat cupidatat non proident, sunt in culpa qui officia deserunt mollit anim id est laborum.</p>
    <p class="body-copy" style="width:250px">Lorem ipsum dolor sit amet, consectetur adipisicing elit, sed do eiusmod tempor incididunt ut labore et dolore magna aliqua. Ut enim ad minim veniam, quis nostrud exercitation ullamco laboris nisi ut aliquip ex ea commodo consequat.</p>
    <p class="body-copy stub">Lorem ipsum dolor sit amet, consectetur a</p>
  </section>
  <section class="column col-right row-main">
    <h2 class="section-title">LOREM IMPOSUM</h2>
    <p class="body-copy">Lorem ipsum dolor sit amet, consectetur adipisicing elit, sed do eiusmod tempor incididunt ut labore et dolore magna aliqua. Ut enim ad minim veniam, quis nostrud exercitation ullamco laboris nisi ut aliquip ex ea commodo consequat. Duis aute irure dolor in reprehenderit in voluptate velit esse cillum dolore eu fugiat nulla pariatur. Excepteur sint occaecat cupidatat non proident, sunt in culpa qui officia deserunt mollit anim id est laborum.</p>
    <p class="body-copy">Lorem ipsum dolor sit amet, consectetur adipisicing elit, sed do eiusmod tempor incididunt ut labore et dolore magna aliqua. Ut enim ad minim veniam, quis nostrud exercitation ullamco laboris nisi ut aliquip ex ea commodo consequat. Duis aute irure dolor in reprehenderit in voluptate velit esse cillum dolore eu fugiat nulla pariatur. Excepteur sint occaecat cupidatat non proident, sunt in culpa qui officia deserunt mollit anim id est laborum.</p>
  </section>

  <div class="brand"><span class="brand-dot"></span>Beyond the Meadow</div>

  <section class="closing">
    <h2 class="section-title">LOREM IMPOSUM</h2>
    <p class="body-copy">Lorem ipsum dolor sit amet, consectetur adipisicing elit, sed do eiusmod tempor incididunt ut labore et dolore magna aliqua. Ut enim ad minim veniam, quis nostrud exercitation ullamco laboris nisi ut aliquip ex ea commodo consequat. Duis aute irure dolor in reprehenderit in voluptate velit esse cillum dolore eu fugiat nulla pariatur. Excepteur sint occaecat cupidatat non proident, sunt in culpa qui officia deserunt mollit anim id est laborum.</p>
  </section>
</main>
</body>
</html>
```